I need a wordpress website for myconsulting company specialized in data privacy

I'm looking for a wordpress website for my consulting company specialized in data privacy (GDPR) and computer science.
The website will serve as entry point to for potential clients.
The website should have the following sections (I'm opened to new ideas):
- Presentation of the company
- General presentation
- Services provided with some details
- Blog/articles with tags (if possible)
- Contact
On every page of the website there should be some references to pages (such as privacy policy, legal information...)
If possible he website should be multinlingual (english and french). I'll personnally take care of the translation in french.
Regarding branding;
- Name of the company: Étienne Roubaud Conseil
- Logo is attached
- For colors to be used see attached PDF for exemple

```html
<!DOCTYPE html>
<html lang="en">
<head>
<meta charset="utf-8">
<title>Étienne Roubaud Conseil</title>
<link href="https://fonts.googleapis.com/css2?family=Michroma&family=Poppins:wght@400;500;600&display=swap" rel="stylesheet">
<style>
:root{
  --teal:#17879a;
  --teal-2:#22a88c;
  --navy:#0c2b48;
  --ink:#555b66;
  --white:#fff;
  --hero-a:#1c2a2c;
  --hero-b:#4a5a5c;
}
*{box-sizing:border-box;margin:0;padding:0}
html,body{width:1200px;height:3727px;overflow:hidden}
body{position:relative;background:var(--white);font-family:"Poppins",sans-serif;color:var(--ink)}
.abs{position:absolute}
.display{font-family:"Michroma",sans-serif;color:var(--navy);text-transform:uppercase;letter-spacing:1px}
.btn{position:absolute;display:flex;align-items:center;justify-content:center;font-family:"Poppins",sans-serif;font-weight:600;font-size:12px;text-transform:uppercase;background:var(--teal);color:var(--white);border-radius:3px}

/* header */
.site-header{left:0;top:0;width:1200px;height:84px;background:var(--white)}
.brand{left:88px;top:24px;display:flex;align-items:center;gap:12px}
.brand-mark{width:30px;height:30px;background:var(--teal)}
.brand-name{font-family:"Michroma",sans-serif;font-size:18px;color:var(--navy);line-height:1}
.nav{left:547px;top:0;height:84px;display:flex;gap:20px;align-items:center;font-size:13px;font-weight:600;color:var(--navy)}
.nav a{color:inherit;text-decoration:none;height:84px;display:flex;align-items:center}
.nav a.active{color:var(--teal);border-top:2px solid var(--teal)}
.header-cta{left:1003px;top:24px;width:108px;height:36px;background:#e6e8ea;color:var(--navy);font-size:11px}

/* hero */
.hero-title{left:88px;top:288px;font-size:52px;line-height:54px;color:var(--white);font-weight:400}
.hero-sub{left:90px;top:408px;font-size:15px;line-height:24px;color:var(--white)}
.hero-btn{left:88px;top:476px;width:137px;height:45px}

/* about */
.eyebrow{font-size:14px;color:var(--teal)}
.section-title{font-size:30px;line-height:40px}
.rule{height:2px;width:48px;background:#d9dde0}
.about-text{left:647px;top:1094px;width:420px;font-size:15px;line-height:25px}
.about-btn{left:646px;top:1243px;width:109px;height:37px;font-size:11px}

/* privacy */
.center{left:0;width:1200px;text-align:center}
.feature{width:260px}
.feature h3{font-family:"Michroma",sans-serif;font-size:13px;line-height:16px;color:var(--navy);font-weight:400;text-transform:uppercase}
.feature p{font-size:13px;line-height:19px;margin-top:12px}
.feature.left{text-align:right}
.emblem{left:500px;top:1662px;width:200px;height:184px;display:flex;flex-direction:column;align-items:center;gap:16px}
.emblem-square{width:140px;height:140px;background:var(--teal);border-radius:6px}
.emblem-name{font-family:"Michroma",sans-serif;font-size:12px;color:var(--navy)}

/* risk band */
.risk-title{top:2080px;font-size:31px;line-height:37px;color:var(--white)}
.risk-text{top:2188px;font-size:15px;line-height:22px;color:var(--white)}
.risk-btn{left:510px;top:2255px;width:180px;height:41px;background:var(--white);color:var(--navy);font-size:11px}

/* blog */
.card{top:2667px;width:331px;height:425px;background:var(--white);box-shadow:0 10px 30px rgba(12,43,72,.1)}
.card-media{width:331px;height:248px}
.card h4{position:absolute;left:34px;top:280px;font-family:"Michroma",sans-serif;font-size:15px;font-weight:400;color:var(--navy)}
.card p{position:absolute;left:34px;top:302px;width:280px;font-size:13px;line-height:21px}
.card a{position:absolute;left:34px;top:379px;font-size:12px;font-weight:600;color:var(--teal)}

/* footer */
.foot-logo{left:160px;top:3430px;width:240px;text-align:center}
.foot-mark{width:56px;height:56px;background:var(--teal);margin:0 auto 10px}
.foot-name{font-family:"Michroma",sans-serif;font-size:16px;color:var(--white)}
.social{top:3542px;width:42px;height:42px;border-radius:50%;background:rgba(255,255,255,.12)}
.foot-col h5{font-family:"Michroma",sans-serif;font-size:17px;font-weight:400;color:var(--white);margin-bottom:14px}
.foot-col li{list-style:none;font-size:12px;line-height:22px;color:#c9d3dc}
.contact li{display:flex;align-items:center;gap:10px;line-height:36px}
.foot-line{left:88px;top:3670px;width:1024px;height:1px;background:rgba(255,255,255,.15)}
.copyright{top:3688px;font-size:13px;color:var(--white)}
.to-top{left:1136px;top:3654px;width:40px;height:40px;border-radius:50%;background:var(--teal)}
</style>
</head>
<body>

<header class="abs site-header">
  <div class="abs brand"><span class="brand-mark"></span><span class="brand-name">Étienne Roubaud Conseil</span></div>
  <nav class="abs nav">
    <a class="active" href="#">HOME</a><a href="#">ABOUT US</a><a href="#">OUR SERVICES</a><a href="#">BLOG</a><a href="#">CONTACT US</a>
    <svg width="16" height="16" viewBox="0 0 16 16" style="margin-left:4px"><circle cx="7" cy="7" r="5" fill="none" stroke="#0c2b48" stroke-width="1.6"/><path d="M11 11l4 4" stroke="#0c2b48" stroke-width="1.6"/></svg>
  </nav>
  <span class="btn header-cta">Get in touch</span>
</header>

<!-- hero -->
<svg class="abs" style="left:0;top:84px" width="1200" height="754" viewBox="0 84 1200 754">
  <defs><linearGradient id="heroGrad" x1="0" x2="1" y1="0" y2="1"><stop offset="0" stop-color="var(--hero-a)"/><stop offset="1" stop-color="var(--hero-b)"/></linearGradient></defs>
  <polygon role="img" aria-label="Photo of two consultants working on a laptop" points="0,84 1200,84 1200,812 775,812 660,710 0,710" fill="url(#heroGrad)"/>
  <polygon points="0,710 650,710 775,812 1200,812 1200,826 770,826 642,722 0,722" fill="var(--teal)"/>
  <polygon points="0,722 642,722 770,826 1200,826 1200,838 765,838 640,734 0,734" fill="#fff"/>
</svg>
<h1 class="abs display hero-title">Consulting<br>Copmany</h1>
<p class="abs display hero-sub">Specialized in data privacy (GDPR)<br>and computer science.</p>
<span class="btn hero-btn">Get started</span>

<!-- about -->
<svg class="abs" style="left:0;top:907px;filter:drop-shadow(0 20px 30px rgba(12,43,72,.15))" width="600" height="560" viewBox="0 0 600 560">
  <defs><linearGradient id="aboutGrad" x1="0" x2="1" y1="0" y2="1"><stop offset="0" stop-color="#0d2a3a"/><stop offset=".6" stop-color="#0e6d8a"/><stop offset="1" stop-color="#0a2233"/></linearGradient></defs>
  <polygon role="img" aria-label="Photo of a person using a tablet with data network lines" points="0,0 575,0 575,473 359,473 297,529 0,529" fill="url(#aboutGrad)"/>
</svg>
<p class="abs display eyebrow" style="left:647px;top:968px">About us</p>
<h2 class="abs display section-title" style="left:647px;top:996px">Étienne Roubaud<br>Conseil</h2>
<div class="abs rule" style="left:647px;top:1078px"></div>
<p class="abs about-text">Lorem Ipsum proin gravida nibh vel velit auctor aliquet aenean sollicitudin, lorem quis bibendum auctor, nisi elit consequat ipsum, nec sagittis sem nibh id elit. Duis sed odio sit amet nibh vulputate cursus a sit amet mauris. Morbi accumsan ipsum velit...</p>
<span class="btn about-btn">Read more</span>

<!-- privacy access control -->
<h2 class="abs center display section-title" style="top:1531px">Privacy access control</h2>
<p class="abs center" style="top:1576px;font-size:15px">Lorem Ipsum proin gravida nibh vel velit auctor aliquet aenean .</p>

<div class="abs feature left" style="left:124px;top:1648px"><h3>Data protection<br>impact assessments</h3><p>Lorem Ipsum is simply dummy text of<br>the printing and typesetting...</p></div>
<div class="abs feature left" style="left:124px;top:1777px"><h3>Processing activity &amp;<br>privacy roles</h3><p>Lorem Ipsum is simply dummy text of<br>the printing and typesetting...</p></div>
<div class="abs feature" style="left:815px;top:1648px"><h3>User and system<br>credentials</h3><p>Lorem Ipsum is simply dummy text of<br>the printing and typesetting...</p></div>
<div class="abs feature" style="left:815px;top:1777px"><h3>Consent flagged<br>authorization</h3><p>Lorem Ipsum is simply dummy text of<br>the printing and typesetting...</p></div>

<svg class="abs" style="left:398px;top:1650px" width="52" height="56" viewBox="0 0 52 56" fill="none" stroke="var(--teal)" stroke-width="1.6"><rect x="2" y="2" width="32" height="44" rx="2"/><path d="M8 12h4M16 12h12M8 22h4M16 22h12M8 32h4M16 32h8"/><circle cx="40" cy="42" r="10"/><circle cx="40" cy="39" r="3"/></svg>
<svg class="abs" style="left:400px;top:1778px" width="48" height="48" viewBox="0 0 48 48" fill="none" stroke="var(--teal)" stroke-width="1.6"><circle cx="24" cy="24" r="22"/><circle cx="24" cy="24" r="15"/><circle cx="24" cy="24" r="7"/></svg>
<svg class="abs" style="left:748px;top:1650px" width="54" height="44" viewBox="0 0 54 44" fill="none" stroke="var(--teal)" stroke-width="1.6"><rect x="2" y="2" width="50" height="38" rx="3"/><path d="M2 10h50"/><circle cx="12" cy="30" r="4"/><path d="M12 20v6M22 28h4M30 28h4M38 28h4M46 28h2"/></svg>
<svg class="abs" style="left:754px;top:1780px" width="46" height="48" viewBox="0 0 46 48" fill="none" stroke="var(--teal)" stroke-width="1.6"><rect x="8" y="2" width="34" height="38" rx="2"/><path d="M14 10h22M14 16h22M14 22h14"/><circle cx="14" cy="34" r="8"/><path d="M10 42l-2 5M18 42l2 5"/></svg>

<div class="abs emblem"><div class="emblem-square"></div><div class="emblem-name">Étienne Roubaud Conseil</div></div>

<!-- risk band -->
<svg class="abs" style="left:0;top:1950px" width="1200" height="558" viewBox="0 0 1200 558">
  <defs><linearGradient id="bandGrad" x1="0" x2="1" y1="0" y2="1"><stop offset="0" stop-color="#138e9d"/><stop offset="1" stop-color="#24a98a"/></linearGradient></defs>
  <polygon role="img" aria-label="Teal background with faint network pattern" points="0,0 1200,0 1200,558 777,558 702,482 0,482" fill="url(#bandGrad)"/>
</svg>
<h2 class="abs center display risk-title">Problem risk and impact<br>assessment</h2>
<div class="abs rule" style="left:576px;top:2163px;background:#fff"></div>
<p class="abs center risk-text">Lorem Ipsum proin gravida nibh vel velit auctor aliquet aenean sollicitudin, lorem quis<br>bibendum auctor, nisi elit consequat ipsum, nec sagittis sem nibh id elit.</p>
<span class="btn risk-btn">Get in touch with us</span>

<!-- blog -->
<h2 class="abs center display section-title" style="top:2586px">Latest blog</h2>
<div class="abs rule" style="left:576px;top:2633px"></div>

<article class="abs card" style="left:88px">
  <div class="card-media" role="img" aria-label="Photo of a team at computers in a dark room" style="background:linear-gradient(135deg,#2b2420,#5a4a3c)"></div>
  <h4>Blog heading here</h4><p>Lorem Ipsum is simply dummy text of the printing and typesetting industry. Lorem Ipsum has been the industry's.</p><a>READ MORE</a>
</article>
<article class="abs card" style="left:433px">
  <div class="card-media" role="img" aria-label="Photo of hands holding a tablet with charts" style="background:linear-gradient(135deg,#3a3a3c,#b9bcc2)"></div>
  <h4>Blog heading here</h4><p>Lorem Ipsum is simply dummy text of the printing and typesetting industry. Lorem Ipsum has been the industry's.</p><a>READ MORE</a>
</article>
<article class="abs card" style="left:779px">
  <div class="card-media" role="img" aria-label="Photo of hands holding a glowing digital globe" style="background:radial-gradient(circle at 55% 45%,#2a7bd8,#0a1a3c 70%)"></div>
  <h4>Blog heading here</h4><p>Lorem Ipsum is simply dummy text of the printing and typesetting industry. Lorem Ipsum has been the industry's.</p><a>READ MORE</a>
</article>

<!-- footer -->
<svg class="abs" style="left:0;top:3180px" width="1200" height="547" viewBox="0 0 1200 547">
  <polygon points="0,0 420,0 545,112 1200,112 1200,124 540,124 415,12 0,12" fill="var(--teal)"/>
  <polygon points="0,31 405,31 535,144 1200,144 1200,547 0,547" fill="var(--navy)"/>
  <polygon points="0,31 405,31 535,144 1200,144 1200,132 540,132 410,19 0,19" fill="#fff"/>
</svg>
<div class="abs foot-logo"><div class="foot-mark"></div><div class="foot-name">Étienne Roubaud Conseil</div></div>
<span class="abs social" style="left:205px" aria-label="Social link"></span>
<span class="abs social" style="left:257px" aria-label="Social link"></span>
<span class="abs social" style="left:308px" aria-label="Social link"></span>

<div class="abs foot-col" style="left:474px;top:3424px"><h5>SERVICES</h5><ul><li>Threat Hunter</li><li>Incident Responder</li><li>Secure Managed IT</li><li>Compliance</li><li>Cyber Security</li><li>Disaster Planning</li></ul></div>
<div class="abs foot-col contact" style="left:688px;top:3424px"><h5>CONTACT</h5><ul>
  <li><svg width="10" height="13" viewBox="0 0 10 13"><path d="M5 0a5 5 0 0 1 5 5c0 4-5 8-5 8S0 9 0 5a5 5 0 0 1 5-5z" fill="var(--teal)"/><circle cx="5" cy="5" r="2" fill="var(--navy)"/></svg>Some goes address here</li>
  <li><svg width="12" height="9" viewBox="0 0 12 9"><rect width="12" height="9" rx="1" fill="var(--teal)"/><path d="M0 1l6 4 6-4" stroke="var(--navy)" fill="none"/></svg>info@email.com</li>
  <li><svg width="12" height="12" viewBox="0 0 12 12"><path d="M2 0l3 3-1.5 2a8 8 0 0 0 3.5 3.5L9 7l3 3-2 2C5 12 0 7 0 2z" fill="var(--teal)"/></svg>+1245 5855 555</li>
</ul></div>
<div class="abs foot-col" style="left:922px;top:3424px"><h5>SUPPORT</h5><ul><li>Contact Us</li><li>FAQ</li><li>Privacy Policy</li><li>Terms &amp; Conditions</li><li>Team</li></ul></div>

<div class="abs foot-line"></div>
<p class="abs center copyright">Copyright 2022. All Rights Reserved.</p>
<span class="abs to-top"><svg width="40" height="40" viewBox="0 0 40 40"><path d="M15 22l5-5 5 5" stroke="#fff" stroke-width="2" fill="none"/></svg></span>

</body>
</html>
```